Wake Ye Lanterns by Dorin Maskey

This is my 2022 holiday saxophone single. I play soprano saxophone on this song and would like a CD design cover for digital release only. The title of the song is "Wake! Ye Lantern Bearers Glow". I did a smooth but groovy rendition of this holiday classic.
Please see my website http://dorinmq.com for my branding color schemes and themes. Would love the design to "feel like Christmas time".

Target Market(s)

Age group 35 and older / Smooth Jazz listening

Industry/Entity Type

Music / Smooth Jazz

Requirements
Must have
• Name: "Dorin Maskey" Song Title: "Wake! Ye Lantern Bearers Glow", Christmas themes
Nice to have
• 1 of the provided photos, incorporate the logo image in some way (feel free to adjust color scheme as needed)

```html
<!DOCTYPE html>
<html lang="en">
<head>
<meta charset="utf-8">
<title>Wake! Ye Lantern Bearers Glow — Dorin Maskey</title>
<link rel="stylesheet" href="https://fonts.googleapis.com/css2?family=Bodoni+Moda:wght@500&family=Oswald:wght@500&family=Poiret+One&display=swap">
<style>
  :root {
    --night: #07061a;
    --deep-violet: #1a1050;
    --ice: #e8fbff;
    --cyan: #3ee4ff;
    --cyan-deep: #0a9fd8;
    --glow: rgba(90, 230, 255, 0.75);
  }
  * { margin: 0; padding: 0; box-sizing: border-box; }
  html, body {
    width: 1200px; height: 1200px; overflow: hidden;
    background: var(--night);
  }
  .cover {
    position: relative;
    width: 1200px; height: 1200px;
    overflow: hidden;
    background:
      radial-gradient(ellipse 520px 420px at 560px 620px, rgba(40, 40, 150, 0.85), transparent 70%),
      radial-gradient(ellipse 900px 700px at 600px 650px, var(--deep-violet), var(--night) 80%);
  }
  .bokeh-field {
    position: absolute; inset: 0;
    background:
      radial-gradient(circle 75px at 80px 110px, rgba(140,108,240,.55), transparent 95%),
      radial-gradient(circle 70px at 170px 240px, rgba(120,90,230,.5), transparent 95%),
      radial-gradient(circle 70px at 860px 110px, rgba(120,90,230,.4), transparent 95%),
      radial-gradient(circle 80px at 1110px 190px, rgba(140,108,240,.55), transparent 95%),
      radial-gradient(circle 70px at 940px 260px, rgba(120,90,230,.45), transparent 95%),
      radial-gradient(circle 75px at 1050px 420px, rgba(130,95,235,.55), transparent 95%),
      radial-gradient(circle 80px at 1160px 560px, rgba(150,110,245,.6), transparent 95%),
      radial-gradient(circle 70px at 920px 560px, rgba(140,108,240,.5), transparent 95%),
      radial-gradient(circle 75px at 60px 440px, rgba(120,90,230,.5), transparent 95%),
      radial-gradient(circle 70px at 250px 440px, rgba(120,90,230,.45), transparent 95%),
      radial-gradient(circle 75px at 110px 700px, rgba(140,108,240,.5), transparent 95%),
      radial-gradient(circle 70px at 220px 820px, rgba(120,90,230,.45), transparent 95%),
      radial-gradient(circle 80px at 90px 1000px, rgba(150,110,245,.6), transparent 95%),
      radial-gradient(circle 80px at 340px 1120px, rgba(140,108,240,.55), transparent 95%),
      radial-gradient(circle 80px at 650px 1070px, rgba(150,110,245,.55), transparent 95%),
      radial-gradient(circle 85px at 960px 1030px, rgba(170,120,250,.6), transparent 95%),
      radial-gradient(circle 75px at 1130px 820px, rgba(150,110,245,.6), transparent 95%),
      radial-gradient(circle 70px at 1100px 1140px, rgba(150,110,245,.5), transparent 95%),
      radial-gradient(circle 70px at 1010px 700px, rgba(140,108,240,.5), transparent 95%);
  }
  .artist-name {
    position: absolute;
    top: 148px; left: 0; width: 100%;
    text-align: center;
    font-family: "Poiret One", "Didot", serif;
    font-size: 76px;
    line-height: 1;
    letter-spacing: 1px;
    color: var(--ice);
  }
  .angel-art {
    position: absolute;
    left: 220px; top: 290px;
    width: 770px; height: 470px;
    background: radial-gradient(closest-side, rgba(150, 240, 255, 0.45), rgba(80, 170, 240, 0.22) 50%, rgba(60, 100, 220, 0.08) 78%, transparent 100%);
  }
  .title {
    position: absolute;
    top: 752px; left: 0; width: 100%;
    text-align: center;
    font-family: "Bodoni Moda", "Didot", serif;
    font-weight: 500;
    font-size: 196px;
    line-height: 1;
    letter-spacing: 6px;
    background: linear-gradient(180deg, var(--cyan-deep), var(--cyan) 55%, #a8f4ff);
    -webkit-background-clip: text;
    background-clip: text;
    color: transparent;
    filter: drop-shadow(0 0 10px rgba(40, 200, 255, 0.45));
  }
  .subtitle {
    position: absolute;
    top: 946px; left: 0; width: 100%;
    text-align: center;
    font-family: "Oswald", "Arial Narrow", sans-serif;
    font-weight: 500;
    font-size: 60px;
    line-height: 1;
    color: var(--ice);
    -webkit-text-stroke: 2px var(--cyan-deep);
    text-shadow: 0 0 12px var(--glow);
  }
  .flare {
    position: absolute;
    left: 770px; top: 805px;
    width: 200px; height: 200px;
    border-radius: 50%;
    background: radial-gradient(circle, #ffffff 0 4%, rgba(220, 230, 255, .6) 10%, rgba(180, 160, 255, .15) 40%, transparent 70%);
  }
  .flare-streak {
    position: absolute;
    left: 640px; top: 903px;
    width: 560px; height: 4px;
    background: linear-gradient(90deg, transparent, rgba(220, 230, 255, .8) 40%, rgba(220, 230, 255, .5) 70%, transparent);
  }
</style>
</head>
<body>
  <main class="cover">
    <div class="bokeh-field" role="img" aria-label="Starry night sky with soft violet bokeh lights"></div>
    <div class="artist-name">DORIN MASKEY</div>
    <div class="angel-art" role="img" aria-label="Glowing neon line illustration of a Christmas herald angel in flight, blowing a trumpet"></div>
    <h1 class="title">WAKE!</h1>
    <h2 class="subtitle">Ye Lantern Bearers Glow</h2>
    <div class="flare-streak"></div>
    <div class="flare"></div>
  </main>
</body>
</html>
```